Tolvern Business Cards

Business card design. dont mind if new logo is suggested.
it would be for a security company.
our clients would be bigger security companies around Australia.
have a logo done but can be replaced. see attaached. like the colors.
Need company name, person name, designation, phone and email on front.
At back company logo and name. website saddress and 2 x license numbers
would like to have 2 different background color for both sidde

Industry/Entity Type

Security

Contact Information for Business Card

round corners, front should be light in color. need logo at back with webaddress and 2 x license numners

Font styles to use
Sans Serif

Colors
f37122
faa54b
f8ba93
0255a3
0592cd
85cae6
b3d448
9bcb3c
ffffff

Requirements
Must have
• see description
Nice to have
• see description
Should not have
• should not be difficult to read or hardd to find information on card.. lets say easy on eyes yet catchy

```html
<!DOCTYPE html>
<html lang="en">
<head>
<meta charset="utf-8">
<title>Tolvern Business Cards</title>
<link href="https://fonts.googleapis.com/css2?family=Open+Sans:wght@400;600;700&display=swap" rel="stylesheet">
<style>
  :root {
    --page-bg: #e9e7e3;
    --card-dark: #323234;
    --card-light: #ffffff;
    --brand-blue: #0255a3;
    --brand-sky: #0592cd;
    --ink: #1b1b1d;
    --ink-soft: #3a3a3d;
  }
  * { margin: 0; padding: 0; box-sizing: border-box; }
  html, body {
    width: 1200px; height: 800px; overflow: hidden;
    background: var(--page-bg);
    font-family: "Open Sans", Arial, sans-serif;
  }
  .canvas {
    width: 1200px; height: 800px;
    display: flex; align-items: center; justify-content: center; gap: 40px;
  }
  .card {
    width: 520px; height: 300px;
    border-radius: 18px;
    position: relative;
    overflow: hidden;
    box-shadow: 0 10px 28px rgba(0,0,0,0.18);
  }
  /* Back side */
  .card-back {
    background: var(--card-dark);
    display: flex; flex-direction: column; align-items: center; justify-content: center;
  }
  .brand {
    display: flex; align-items: center; gap: 14px;
  }
  .brand-dot {
    width: 30px; height: 30px; border-radius: 50%;
    background: var(--brand-sky);
  }
  .brand-name {
    font-size: 44px; font-weight: 600; letter-spacing: 4px;
    text-transform: uppercase;
  }
  .card-back .brand-name { color: var(--brand-sky); }
  .website {
    margin-top: 22px;
    font-size: 15px; color: var(--brand-blue);
    letter-spacing: 0.5px;
  }
  /* Front side */
  .card-front { background: var(--card-light); }
  .card-front .brand {
    position: absolute; top: 38px; right: 36px;
  }
  .card-front .brand-dot { width: 24px; height: 24px; background: var(--brand-blue); }
  .card-front .brand-name { font-size: 34px; color: var(--brand-blue); letter-spacing: 3px; }
  .person {
    position: absolute; left: 0; top: 120px;
    padding-left: 30px;
    border-left: 10px solid var(--brand-blue);
  }
  .person-name { font-size: 28px; color: var(--ink); line-height: 1.1; font-weight: 400; }
  .person-name strong { font-weight: 700; }
  .person-title { font-size: 16px; color: var(--brand-blue); margin-top: 2px; }
  .contacts {
    position: absolute; left: 40px; top: 206px;
    list-style: none;
  }
  .contacts li {
    display: flex; align-items: center; gap: 10px;
    font-size: 16px; color: var(--ink-soft); margin-bottom: 6px;
  }
  .contacts svg { width: 16px; height: 16px; fill: var(--brand-blue); }
  .rule {
    position: absolute; left: 0; top: 258px;
    width: 318px; height: 2px; background: var(--brand-blue);
  }
  .licence {
    position: absolute; left: 326px; top: 248px;
    font-size: 15px; color: var(--brand-blue); white-space: nowrap;
  }
</style>
</head>
<body>
<main class="canvas">
  <section class="card card-back" aria-label="Card back">
    <div class="brand">
      <span class="brand-dot"></span>
      <span class="brand-name">Tolvern</span>
    </div>
    <p class="website">www.tolvernsecurity.com</p>
  </section>

  <section class="card card-front" aria-label="Card front">
    <div class="brand">
      <span class="brand-dot"></span>
      <span class="brand-name">Tolvern</span>
    </div>
    <div class="person">
      <h1 class="person-name">Your <strong>Name</strong></h1>
      <p class="person-title">Job Title</p>
    </div>
    <ul class="contacts">
      <li>
        <svg viewBox="0 0 16 16" aria-hidden="true"><path d="M3 1h3l1.5 4-2 1.2a9 9 0 0 0 4.3 4.3L11 8.5l4 1.5v3a2 2 0 0 1-2 2A12 12 0 0 1 1 3a2 2 0 0 1 2-2z"/></svg>
        000 000 0000
      </li>
      <li>
        <svg viewBox="0 0 16 16" aria-hidden="true"><path d="M1 3h14v10H1z M1 3l7 6 7-6" fill="none" stroke="#0255a3" stroke-width="1.6"/></svg>
        youremail@tolvern.com
      </li>
    </ul>
    <div class="rule"></div>
    <p class="licence">Lic.No.0000000 | 0000000</p>
  </section>
</main>
</body>
</html>
```